Business Card Design for a Personal Trainer

I need a business card design for my job as a personal trainer. It should have a unique, modern and exclusive design. On the front there should be only my logo with my name and my job. 0163/2918374 Tobias Kellinger Lindenfeldweg 14 80412 Munich Germany The most important contact information is the web adress. it can be bigger than the rest, but its not necessary. The card should be 8,5cmx5,5cm big. Font: Roboto. Colors: black, white, gray, 56c1ff.

```html
<!DOCTYPE html>
<html lang="de">
<head>
<meta charset="utf-8">
<title>Tobias Kellinger – Personal Trainer Business Card</title>
<link href="https://fonts.googleapis.com/css2?family=Roboto:wght@300;400;500&display=swap" rel="stylesheet">
<style>
  :root {
    --scene-bg: #3d444c;
    --card-black: #141414;
    --card-navy-dark: #0b1620;
    --card-navy: #1c3447;
    --accent: #56c1ff;
    --white: #ffffff;
    --gray: #b9c0c7;
    --photo-dark: #2a2c30;
    --photo-mid: #5a5e64;
  }
  * { box-sizing: border-box; margin: 0; padding: 0; }
  html, body {
    width: 1200px; height: 960px; overflow: hidden;
    background: var(--scene-bg);
    font-family: "Roboto", Arial, sans-serif;
  }
  .canvas { position: relative; width: 1200px; height: 960px; }

  .card {
    position: absolute;
    width: 520px; height: 336px;
    border-radius: 4px;
    overflow: hidden;
    box-shadow: 0 18px 40px rgba(0,0,0,.45);
  }

  /* Front */
  .card-front {
    left: 80px; top: 130px;
    background: var(--card-black);
    display: flex; align-items: center; justify-content: center;
  }
  .brand { display: flex; flex-direction: column; align-items: center; }
  .brand-square {
    width: 54px; height: 54px;
    border: 6px solid var(--white);
    margin-bottom: 22px;
  }
  .brand-name {
    color: var(--white);
    font-weight: 400;
    font-size: 34px;
    letter-spacing: 2px;
    text-transform: uppercase;
  }
  .brand-role {
    display: flex; align-items: center; gap: 10px;
    margin-top: 6px;
    color: var(--white);
    font-size: 12px; font-weight: 300;
    letter-spacing: 5px; text-transform: uppercase;
  }
  .brand-role::before, .brand-role::after {
    content: ""; width: 70px; height: 1px; background: var(--white);
  }

  /* Back */
  .card-back {
    left: 600px; top: 494px;
    background: radial-gradient(ellipse at 60% 40%, var(--card-navy) 0%, var(--card-navy-dark) 80%);
  }
  .portrait {
    position: absolute;
    left: 36px; bottom: 0;
    width: 200px; height: 270px;
    background: linear-gradient(180deg, var(--photo-mid) 0%, var(--photo-dark) 70%);
    border-radius: 90px 90px 0 0;
    opacity: .9;
  }
  .divider {
    position: absolute;
    left: 262px; top: 86px;
    width: 3px; height: 190px;
    background: var(--accent);
  }
  .contact {
    position: absolute;
    left: 282px; top: 80px;
    color: var(--gray);
    font-weight: 300;
    font-size: 14px;
    line-height: 1.35;
  }
  .contact-name { color: var(--accent); font-size: 22px; font-weight: 400; line-height: 1.1; }
  .contact-role { font-size: 10px; margin-bottom: 4px; }
  .contact-phone { color: var(--accent); font-size: 24px; font-weight: 400; margin-bottom: 2px; }
  .contact-address { margin-bottom: 12px; }
</style>
</head>
<body>
<main class="canvas">
  <section class="card card-front" aria-label="Card front">
    <div class="brand">
      <div class="brand-square" aria-hidden="true"></div>
      <div class="brand-name">Tobias Kellinger</div>
      <div class="brand-role">Personal Trainer</div>
    </div>
  </section>

  <section class="card card-back" aria-label="Card back">
    <div class="portrait" role="img" aria-label="Black and white portrait photo of the trainer with arms crossed"></div>
    <div class="divider"></div>
    <div class="contact">
      <p class="contact-name">Tobias Kellinger</p>
      <p class="contact-role">Personal Trainer</p>
      <p class="contact-phone">0163 2918 - 374</p>
      <p class="contact-address">Lindenfeldweg 14<br>80412 München</p>
      <p>t.kellinger@trainmail.de<br>www.tobiaskellinger.de</p>
    </div>
  </section>
</main>
</body>
</html>
```